Loomtrix Business Cards - Strong Existing Branding

We need a new business card design. We have strong existing branding. The card should have text placeholder for

EXAMPLES IN QUOTES

Name: "Carl Ostrander"
Title: "CEO & Co-Founder"
Address: "482 N Pellam Ave" "Houston, TX 77241"
Email: "carl@loomtrix.example"
Office: "855-217-3904 ext 300"
Cell: "404-382-5916"
Web: http://loomtrix.example
Twitter: @loomtrix

Target Market(s)

Manufacturers that don't do software

Industry/Entity Type

Business

Requirements
Must have
• We use some lines and circles like fake circuit board... see our logo for example. This should be on the card somewhere.

Should use Bebas font

See : http://loomtrix.example

Our colors are

#43292E
#F18932

```html
<!DOCTYPE html>
<html lang="en">
<head>
<meta charset="utf-8">
<title>Loomtrix Business Cards</title>
<link rel="stylesheet" href="https://fonts.googleapis.com/css2?family=Bebas+Neue&display=swap">
<style>
  :root {
    --brand-plum: #43292E;
    --card-dark: #3a2327;
    --brand-orange: #F18932;
    --stage: #2b2b2d;
  }
  * { box-sizing: border-box; margin: 0; padding: 0; }
  html, body { width: 1200px; height: 1000px; overflow: hidden; }
  body {
    background: var(--stage);
    position: relative;
    font-family: "Bebas Neue", "Arial Narrow", sans-serif;
  }
  .card {
    position: absolute;
    width: 540px;
    height: 310px;
    border-radius: 8px;
    overflow: hidden;
    background: var(--card-dark);
    box-shadow: 0 14px 30px rgba(0,0,0,.45);
  }
  .card--back { left: 590px; top: 150px; }
  .card--front { left: 70px; top: 530px; }

  .wordmark {
    position: absolute;
    left: 0; right: 0;
    text-align: center;
    font-size: 72px;
    line-height: 1;
    letter-spacing: 1px;
  }
  .card--back .wordmark { color: var(--brand-orange); top: 120px; }

  .front-band {
    position: absolute;
    left: 0; top: 0;
    width: 540px; height: 150px;
    background: var(--brand-orange);
  }
  .front-band .wordmark { color: var(--card-dark); top: 40px; }

  .circuit {
    position: absolute;
    left: 0; top: 0;
    width: 540px; height: 310px;
  }
  .circuit line, .circuit polyline { stroke: var(--brand-orange); stroke-width: 1.6; fill: none; }
  .circuit circle { stroke: var(--brand-orange); stroke-width: 1.6; fill: var(--card-dark); }

  .contact-list {
    position: absolute;
    left: 40px; top: 162px;
    list-style: none;
    color: var(--brand-orange);
    font-size: 15px;
    line-height: 18px;
    letter-spacing: .5px;
  }

  .holder {
    position: absolute;
    left: 318px; top: 226px;
    color: var(--brand-orange);
    line-height: 1;
  }
  .holder-name { font-size: 28px; letter-spacing: 1px; }
  .holder-title { font-size: 20px; letter-spacing: 1px; margin-top: 6px; }
</style>
</head>
<body>

  <section class="card card--back" aria-label="Card back">
    <div class="wordmark">Loomtrix</div>
  </section>

  <section class="card card--front" aria-label="Card front">
    <div class="front-band">
      <div class="wordmark">Loomtrix</div>
    </div>

    <svg class="circuit" viewBox="0 0 540 310" aria-hidden="true">
      <line x1="22" y1="150" x2="22" y2="252"/>
      <line x1="22" y1="171" x2="34" y2="171"/>
      <line x1="22" y1="189" x2="34" y2="189"/>
      <line x1="22" y1="207" x2="34" y2="207"/>
      <line x1="22" y1="225" x2="34" y2="225"/>
      <line x1="22" y1="243" x2="34" y2="243"/>
      <circle cx="22" cy="171" r="4"/>
      <circle cx="22" cy="189" r="4"/>
      <circle cx="22" cy="207" r="4"/>
      <circle cx="22" cy="225" r="4"/>
      <circle cx="22" cy="243" r="4"/>
      <polyline points="306,214 512,214 512,150"/>
      <polyline points="306,214 306,300 330,300"/>
      <circle cx="300" cy="214" r="5"/>
    </svg>

    <ul class="contact-list">
      <li>855-217-3904 ext 300</li>
      <li>404-382-5916</li>
      <li>carl@loomtrix.example</li>
      <li>http://loomtrix.example</li>
      <li>@loomtrix</li>
      <li>482 N Pellam Ave</li>
      <li>Houston, TX 77241</li>
    </ul>

    <div class="holder">
      <div class="holder-name">Carl Ostrander</div>
      <div class="holder-title">CEO &amp; Co-Founder</div>
    </div>
  </section>

</body>
</html>
```